Website Design for ZORVENTA.TV and BELUMKO.TV online televisions

Basically an online television program which consist of video sequential playing (base on youtube etc) as well as streaming direct from our studio. We have a draft model which can be seen at [login to view URL] which we use standard joomla template with special c

```html
<!DOCTYPE html>
<html lang="en">
<head>
<meta charset="utf-8">
<title>ZORVENTA.TV</title>
<link href="https://fonts.googleapis.com/css2?family=Cinzel:wght@400&family=Source+Sans+3:wght@400;600;700&display=swap" rel="stylesheet">
<style>
  :root{
    --bg-dark:#151b22;
    --bg-mid:#222a33;
    --panel:#0b0c0e;
    --nav-top:#2a2d31;
    --nav-bottom:#0f1012;
    --accent:#3aa0e0;
    --text-light:#e8ecef;
    --text-muted:#c9ced3;
    --link:#6f9fbf;
    --box-light:#f2f2f2;
    --box-dark:#bdbdbd;
    --ink:#1a1a1a;
  }
  *{margin:0;padding:0;box-sizing:border-box}
  html,body{width:850px;height:1200px;overflow:hidden}
  body{
    position:relative;
    background:radial-gradient(ellipse at 50% 10%, #2c3844 0%, var(--bg-mid) 35%, var(--bg-dark) 75%);
    font-family:"Source Sans 3",sans-serif;
    color:var(--text-light);
  }
  .abs{position:absolute}

  .account-bar{left:634px;top:0;width:117px;height:19px;display:flex;
    background:linear-gradient(#1d5c78,#0f3a4f);border-radius:0 0 3px 3px}
  .account-bar a{flex:1;text-align:center;font-size:8px;line-height:19px;color:#cfe3ee;text-decoration:none;letter-spacing:.3px}
  .account-bar a+a{border-left:1px solid #0a2a3a}

  .brand{left:102px;top:14px;display:flex;align-items:center;gap:14px}
  .brand-mark{width:80px;height:80px;border-radius:50%;border:2px solid #d8d8d8}
  .brand-name{font-family:"Cinzel",serif;font-size:22px;letter-spacing:2px;color:#e6e6e6}

  .social{left:512px;top:49px;display:flex;gap:5px}
  .social span{width:19px;height:19px;border-radius:3px}
  .social .s1{background:#3a76c2}.social .s2{background:#2fb2d0}.social .s3{background:#c8261e}

  .search{left:595px;top:48px;width:156px;height:21px;border-radius:11px;
    background:linear-gradient(#f4f4f4,#d6d6d6);font-size:8px;color:#333;padding-left:11px;line-height:21px}
  .search svg{position:absolute;right:9px;top:4px}

  .main-nav{left:101px;top:110px;width:650px;height:36px;display:flex;
    background:linear-gradient(var(--nav-top),var(--nav-bottom));box-shadow:0 3px 8px rgba(0,0,0,.6)}
  .main-nav a{flex:none;font-size:11px;font-weight:700;color:#f2f2f2;text-decoration:none;line-height:36px;
    white-space:nowrap;text-align:center;border-right:1px solid #3a3d41}
  .main-nav a:last-child{border-right:0}
  .main-nav a.active{color:var(--accent)}
  .n1{width:52px}.n2{width:57px}.n3{width:83px}.n4{width:97px}
  .n5{width:78px}.n6{width:103px}.n7{width:113px}.n8{width:67px}

  .player-panel{left:101px;top:146px;width:650px;height:351px;background:var(--panel);
    box-shadow:0 12px 24px rgba(0,0,0,.7)}
  .player-video{left:116px;top:164px;width:619px;height:299px;
    background:radial-gradient(ellipse at 40% 50%, #5a4a3e 0%, #3a3530 45%, #4f6a45 100%)}
  .play-btn{left:397px;top:299px;width:58px;height:44px;border-radius:8px;background:rgba(20,20,20,.55)}
  .controls{left:116px;top:463px;width:633px;height:17px;background:#141414;font-size:8px;color:#ddd}
  .controls .t1{position:absolute;left:24px;top:3px}
  .controls .t2{position:absolute;right:44px;top:3px}
  .controls .track{position:absolute;left:56px;right:90px;top:3px;height:11px;background:#1e1e1e}
  .controls .buffer{position:absolute;left:90px;width:60px;top:0;bottom:0;background:#262626}

  .video-box{left:101px;width:648px;height:151px;border-radius:3px;
    background:linear-gradient(var(--box-light),var(--box-dark));box-shadow:0 4px 10px rgba(0,0,0,.6)}
  .video-box h2{position:absolute;left:12px;top:10px;font-size:16px;font-weight:400;color:var(--ink);letter-spacing:-.2px}
  .video-box .rule{position:absolute;left:12px;right:13px;top:30px;height:1px;background:#333}
  .thumb{position:absolute;top:39px;width:147px;height:81px;border:2px solid #111}
  .thumb::after{content:"";position:absolute;left:62px;top:28px;width:22px;height:20px;border-radius:3px;background:rgba(60,60,60,.55)}
  .th1{left:11px;background:linear-gradient(#141414,#050505)}
  .th2{left:171px;background:linear-gradient(135deg,#c9b98a,#7fb2d2 55%,#d2c494)}
  .th3{left:329px;background:radial-gradient(ellipse at 55% 45%, #c9a06f 0%, #7a2a20 55%, #1a0b08 100%)}
  .th4{left:488px;background:linear-gradient(#0c0c0c,#1b1b1b)}
  .view-more{position:absolute;right:13px;top:125px;width:61px;height:17px;border:1px solid #888;border-radius:3px;
    background:linear-gradient(#fafafa,#cfcfcf);font-size:9px;font-weight:700;color:#333;text-align:center;line-height:15px}

  .site-footer{left:101px;top:916px;width:650px;height:240px;background:var(--panel);box-shadow:0 10px 20px rgba(0,0,0,.7)}
  .about-col{position:absolute;left:12px;top:18px;width:390px}
  .about-col h3{font-size:16px;font-weight:400;color:#fff;margin-bottom:1px}
  .about-col p{font-size:9px;line-height:13.2px;color:var(--text-muted)}
  .about-col h3.media{margin-top:16px}
  .quick-links{position:absolute;left:493px;top:18px}
  .quick-links h4{font-size:12.5px;font-weight:400;color:var(--link);margin-bottom:6px}
  .quick-links a{display:block;font-size:9px;line-height:18.8px;color:var(--link);text-decoration:none}
  .footer-bar{position:absolute;left:11px;top:206px;width:625px;height:25px;background:linear-gradient(#222,#111);
    font-size:8px;color:#cfcfcf;line-height:25px;padding-left:9px}
</style>
</head>
<body>
  <nav class="account-bar abs"><a href="#">LOGIN</a><a href="#">REGISTER</a></nav>

  <div class="brand abs">
    <span class="brand-mark"></span>
    <span class="brand-name">ZORVENTA</span>
  </div>

  <div class="social abs"><span class="s1"></span><span class="s2"></span><span class="s3"></span></div>

  <div class="search abs">Search
    <svg width="12" height="12" viewBox="0 0 12 12"><circle cx="7" cy="5" r="3.6" fill="none" stroke="#666" stroke-width="1.2"/><line x1="4.4" y1="7.6" x2="1.2" y2="10.8" stroke="#666" stroke-width="1.4"/></svg>
  </div>

  <nav class="main-nav abs">
    <a class="n1 active" href="#">HOME</a><a class="n2" href="#">ABOUT</a><a class="n3" href="#">TOP VIDEOS</a><a class="n4" href="#">NEW RELEASES</a><a class="n5" href="#">PRODUCTS</a><a class="n6" href="#">MOST POPULAR</a><a class="n7" href="#">TOP DOWNLOADS</a><a class="n8" href="#">CONTACT</a>
  </nav>

  <div class="player-panel abs"></div>
  <div class="player-video abs" role="img" aria-label="Video frame: two boys in caps reciting from a book with a microphone"></div>
  <div class="play-btn abs"><svg width="58" height="44"><polygon points="23,13 38,22 23,31" fill="#8a8a8a"/></svg></div>
  <div class="controls abs">
    <svg class="abs" style="left:9px;top:4px" width="8" height="9"><rect x="0" y="0" width="2.5" height="9" fill="#eee"/><rect x="5" y="0" width="2.5" height="9" fill="#eee"/></svg>
    <span class="t1">10:15</span>
    <div class="track"><div class="buffer"></div></div>
    <span class="t2">02:46</span>
    <svg class="abs" style="right:20px;top:3px" width="11" height="10"><polygon points="0,3 3,3 7,0 7,10 3,7 0,7" fill="#eee"/></svg>
    <svg class="abs" style="right:4px;top:3px" width="10" height="10"><rect x="1" y="1" width="8" height="8" fill="none" stroke="#eee" stroke-width="1.3"/></svg>
  </div>

  <section class="video-box abs" style="top:541px">
    <h2>MOST VIEWED</h2><div class="rule"></div>
    <div class="thumb th1" role="img" aria-label="Event announcement title card"></div>
    <div class="thumb th2" role="img" aria-label="Illustrated map scene"></div>
    <div class="thumb th3" role="img" aria-label="Historical portrait painting"></div>
    <div class="thumb th4" role="img" aria-label="Program title card"></div>
    <div class="view-more">View More</div>
  </section>

  <section class="video-box abs" style="top:714px">
    <h2>LATEST VIDEOS</h2><div class="rule"></div>
    <div class="thumb th1" role="img" aria-label="Event announcement title card"></div>
    <div class="thumb th2" role="img" aria-label="Illustrated map scene"></div>
    <div class="thumb th3" role="img" aria-label="Historical portrait painting"></div>
    <div class="thumb th4" role="img" aria-label="Program title card"></div>
    <div class="view-more">View More</div>
  </section>

  <footer class="site-footer abs">
    <div class="about-col">
      <h3>Zorventa TV</h3>
      <p>Lorem Ipsum is simply dummy text of the printing and typesetting industry. Lorem Ipsum has been the industry's standard dummy text ever since the 1500s, when an unknown printer took a galley of type and scrambled it to make a type specimen book. It<br>hasLorem Ipsum is simply dummy text of the printing and typesetting industry. Lorem Ipsum has been the industry's standard dummy text ever since the 1500s, when an unknown printer took a galley of type and scrambled it to make a type specimen book. It has</p>
      <h3 class="media">In The Media</h3>
      <p>Lorem Ipsum is simply dummy text of the printing and typesetting industry. Lorem Ipsum has been the industry's standard dummy text ever since the 1500s, when an unknown printer took a galley of type and scrambled it to make a type specimen book. It</p>
    </div>
    <div class="quick-links">
      <h4>QUICK LINKS</h4>
      <a href="#">Terms</a><a href="#">Privacy Policy</a><a href="#">Faqs</a><a href="#">About</a><a href="#">Contact</a><a href="#">Login</a><a href="#">Videos</a>
    </div>
    <div class="footer-bar">Copyright © 2012. ZORVENTA. All Rights Reserved.</div>
  </footer>
</body>
</html>
```